Existing graphics (3D cube) should be made more understandable

Hi,
I would like to make my 3D cube more understandable, but it should also be more presentable. I have attached a detailed description as an attachment. I think the image so far is good, but if we can improve it (more understandable and prettier), I would be happy.
BR
Tor

Target Market(s)

Students, Teachers, Prof.

Colors
0054AA
0677BA
7BADD7
CADEEF
E8F1F8
0094D4
00A9DD
6FCCEA
C7EBF8
E9F6FB
00AB8E
00BBA5
67D7C9
C6EFE9
E9F9F6
59FF00
82FF00
B8FF75
E3FFCB
F4FFEA

Requirements
Must have
• please see attachment
Nice to have
• please see attachment
Should not have
• please see attachment

```html
<!DOCTYPE html>
<html lang="de">
<head>
<meta charset="utf-8">
<title>Führungskräfte-Würfel</title>
<link rel="stylesheet" href="https://fonts.googleapis.com/css2?family=Noto+Sans:wght@400;700&display=swap">
<style>
  :root {
    --paper: #ffffff;
    --ink: #14253a;
    --axis: #0054AA;
    --edge: #2c4a6b;
    --guide: #7BADD7;

    --leader-face: #CADEEF;
    --leader-top: #E8F1F8;
    --leader-accent: #0054AA;

    --both-face: #C6EFE9;
    --both-top: #E9F9F6;
    --both-side: #C6EFE9;
    --both-accent: #00AB8E;

    --manager-face: #C7EBF8;
    --manager-accent: #0094D4;

    --none-face: #E8F1F8;
    --none-accent: #7BADD7;

    --ambi-face: #E3FFCB;
    --ambi-top: #F4FFEA;
    --ambi-accent: #59FF00;

    --back-side: #E9F6FB;
  }
  html, body {
    margin: 0;
    padding: 0;
    width: 1200px;
    height: 840px;
    overflow: hidden;
    background: var(--paper);
  }
  .cube-diagram {
    display: block;
    width: 1200px;
    height: 840px;
    font-family: "Noto Sans", "Segoe UI", Arial, sans-serif;
  }
  .axis { stroke: var(--axis); stroke-width: 2; fill: none; }
  .arrowhead { fill: var(--axis); }
  .edge { stroke: var(--edge); stroke-width: 1.4; fill: none; stroke-linejoin: round; }
  .guide { stroke: var(--guide); stroke-width: 1.4; stroke-dasharray: 7 6; fill: none; }

  .cell { stroke: none; }
  .cell-leader { fill: var(--leader-face); }
  .cell-leader-top { fill: var(--leader-top); }
  .cell-both { fill: var(--both-face); }
  .cell-both-top { fill: var(--both-top); }
  .cell-both-side { fill: var(--both-side); opacity: 0.7; }
  .cell-manager { fill: var(--manager-face); }
  .cell-none { fill: var(--none-face); }
  .cell-ambi { fill: var(--ambi-face); }
  .cell-ambi-top { fill: var(--ambi-top); }
  .cell-back { fill: var(--back-side); }

  text { fill: var(--ink); dominant-baseline: middle; }
  .axis-title { font-size: 18.5px; }
  .scale-mark { font-size: 14px; font-weight: 700; letter-spacing: 0.3px; fill: var(--axis); }
  .depth-mark { font-size: 18.5px; font-weight: 700; fill: var(--axis); }
  .cell-title { font-size: 13.5px; font-weight: 700; text-anchor: middle; }
  .cell-text { font-size: 13.5px; text-anchor: middle; }
  .type-marker { font-size: 23px; font-weight: 700; }
  .marker-dot { stroke: var(--ink); stroke-width: 1; }
  .dot-leader { fill: var(--leader-accent); }
  .dot-both { fill: var(--both-accent); }
  .dot-manager { fill: var(--manager-accent); }
  .dot-none { fill: var(--none-accent); }
  .dot-ambi { fill: var(--ambi-accent); }
</style>
</head>
<body>
<svg class="cube-diagram" viewBox="0 0 1200 840" xmlns="http://www.w3.org/2000/svg" role="img" aria-label="Würfelmodell der Führungskräfte-Kategorien nach Exploration, Exploitation und Flexibilität">

  <!-- cell fills: right face -->
  <polygon class="cell cell-back" points="532,499 843,397 843,582 532,683"/>
  <polygon class="cell cell-both-side" points="532,315 681,267 681,450 532,499"/>
  <polygon class="cell cell-ambi" points="681,267 843,215 843,397 681,450"/>

  <!-- cell fills: top face -->
  <polygon class="cell cell-leader-top" points="238,263 549,164 689,188 385,289"/>
  <polygon class="cell cell-both-top" points="385,289 532,240 681,267 532,315"/>
  <polygon class="cell cell-ambi-top" points="532,240 689,188 843,215 681,267"/>

  <!-- cell fills: front face -->
  <polygon class="cell cell-leader" points="238,263 385,289 385,474 238,448"/>
  <polygon class="cell cell-both" points="385,289 532,315 532,499 385,474"/>
  <polygon class="cell cell-none" points="238,448 385,474 385,658 238,632"/>
  <polygon class="cell cell-manager" points="385,474 532,499 532,683 385,658"/>

  <!-- guide line along depth -->
  <line class="guide" x1="247" y1="628" x2="842" y2="433"/>

  <!-- cube: front face -->
  <polygon class="edge" points="238,263 532,315 532,683 238,632"/>
  <line class="edge" x1="385" y1="289" x2="385" y2="658"/>
  <line class="edge" x1="238" y1="448" x2="532" y2="499"/>

  <!-- cube: top face -->
  <polygon class="edge" points="238,263 549,164 843,215 532,315"/>
  <line class="edge" x1="385" y1="289" x2="689" y2="188"/>
  <line class="edge" x1="532" y1="242" x2="681" y2="267"/>

  <!-- cube: right face -->
  <polygon class="edge" points="532,315 843,215 843,582 532,683"/>
  <line class="edge" x1="532" y1="499" x2="843" y2="397"/>
  <line class="edge" x1="681" y1="267" x2="681" y2="450"/>

  <!-- vertical axis -->
  <line class="axis" x1="238" y1="632" x2="238" y2="148"/>
  <path class="arrowhead" d="M238 141 L246 157 L238 153 L230 157 Z"/>

  <!-- horizontal axis -->
  <line class="axis" x1="238" y1="632" x2="662" y2="704"/>
  <path class="arrowhead" d="M669 705 L652 710 L655 704 L653 697 Z"/>

  <!-- depth axis -->
  <line class="axis" x1="845" y1="430" x2="893" y2="414"/>
  <path class="arrowhead" d="M900 412 L886 424 L887 417 L881 412 Z"/>

  <!-- axis titles -->
  <text class="axis-title" x="128" y="89">Exploration, Opening</text>
  <text class="axis-title" x="128" y="114">Leadership, Leader-Rolle</text>

  <text class="axis-title" x="609" y="739">Exploitation, Closing</text>
  <text class="axis-title" x="609" y="764">Leadership, Manager-Rolle</text>

  <text class="axis-title" x="873" y="247">Flexibilität, um zwischen</text>
  <text class="axis-title" x="873" y="272">Exploration und</text>
  <text class="axis-title" x="873" y="298">Exploitation, Opening und</text>
  <text class="axis-title" x="873" y="323">Closing Leadership, Leader-</text>
  <text class="axis-title" x="873" y="349">und Manager-Rolle</text>
  <text class="axis-title" x="873" y="374">wechseln zu können</text>

  <!-- scale marks -->
  <text class="scale-mark" x="173" y="263">STARK</text>
  <text class="scale-mark" x="162" y="446">MITTEL</text>
  <text class="scale-mark" x="144" y="631">SCHWACH</text>
  <text class="depth-mark" x="177" y="663">Gering</text>
  <text class="scale-mark" x="353" y="676">MITTEL</text>
  <text class="scale-mark" x="513" y="706">STARK</text>
  <text class="depth-mark" x="890" y="435">Hoch</text>

  <!-- Kategorie I -->
  <text class="cell-title" x="312" y="347">KATEGORIE I:</text>
  <text class="cell-text" x="312" y="367">Führungskraft fürs</text>
  <text class="cell-text" x="312" y="386">Leadership (L)</text>
  <circle class="marker-dot dot-leader" cx="342" cy="436" r="4.5"/>
  <text class="type-marker" x="350" y="437">L</text>

  <!-- Kategorie II -->
  <text class="cell-title" x="460" y="350">KATEGORIE II:</text>
  <text class="cell-text" x="460" y="369">Führungskraft fürs</text>
  <text class="cell-text" x="460" y="389">Leadership und</text>
  <text class="cell-text" x="460" y="408">Management (LM)</text>
  <circle class="marker-dot dot-both" cx="463" cy="459" r="4.5"/>
  <text class="type-marker" x="473" y="460">LM</text>

  <!-- Kategorie III -->
  <text class="cell-title" x="762" y="292">KATEGORIE III:</text>
  <text class="cell-text" x="762" y="311">Führungskraft fürs</text>
  <text class="cell-text" x="762" y="330">Ambidextrous</text>
  <text class="cell-text" x="762" y="349">Leadership (A)</text>
  <circle class="marker-dot dot-ambi" cx="743" cy="378" r="4.5"/>
  <text class="type-marker" x="752" y="379">A</text>

  <!-- Kategorie IV -->
  <text class="cell-title" x="460" y="534">KATEGORIE IV:</text>
  <text class="cell-text" x="460" y="553">Führungskraft fürs</text>
  <text class="cell-text" x="460" y="572">Management (M)</text>
  <circle class="marker-dot dot-manager" cx="479" cy="639" r="4.5"/>
  <text class="type-marker" x="488" y="640">M</text>

  <!-- Kategorie V -->
  <text class="cell-title" x="307" y="488">KATEGORIE V:</text>
  <text class="cell-text" x="307" y="508">Weder fürs</text>
  <text class="cell-text" x="307" y="527">Management</text>
  <text class="cell-text" x="307" y="546">noch fürs</text>
  <text class="cell-text" x="307" y="565">Leadership</text>
  <text class="cell-text" x="307" y="584">geeignet (N)</text>
  <circle class="marker-dot dot-none" cx="332" cy="624" r="4.5"/>
  <text class="type-marker" x="340" y="625">N</text>
</svg>
</body>
</html>
```